Vemra. Packaging for mood-boosting energy drink mix. Upbeat and uplifting.

I need a mockup of a pouch package + a stick. I included an image of a Aqua Tarn pouch + stick for reference. I do not have a die line for the pouch, so feel free to just use the same relative dimensions for the pouch and create a rendering. Here are the specifications for the packaging that I need:
1. The logo is included in the uploaded files. Please use the one that says "bright day spark" beneath "vemra." The logo should take up about the top 1/3 to 1/2 of the pouch.
2. The pouch should be mostly white, especially behind the logo, but feel free to explore yellow or orange for the bottom 1/2 to 2/3 of the packaging.
3. In the center of the packaging, below the logo, please have the product name appear, "mood-boosting energy drink mix" similar to where "Fluid Amplifier" is placed.
4. Below that, create an image of a glass with a stick pouring into it like in the Aqua Tarn pouch.
5. Below the glass, in the bottom center of the package, include "16 sticks. Net Wt. 4 oz. (114 g)
6. On the left side, please include callouts, from top to bottom, "energy blend (80mg caffeine, taurine) + happy blend (saffron, st. john's wort, rhodiola).
7. On the right side, please include callouts, from top to bottom, "electrolytes + vitamins + 0g sugar"
8. Somewhere else on the front of the packaging, please include the flavor name "golden berry," perhaps where they do on the aqua tarn pouch.
9. For the stick, use your creativity.
10. There is no back of packaging to design for this project.

Target Market(s)

My target consumer leads a very active lifestyle and cares deeply about health & wellness.

Colors
0094D4
00A9DD
6FCCEA
C7EBF8
E9F6FB
FFC000
F8CF3A
FAE287
FDF2CF
FEFAEE
F0912C
F2A743
F7CA91
FBE8D2
FDF5EE
EE7325
F08F49
F5BC92
FAE3D3
FDF4ED

Requirements
Must have
• My packaging must make people feel good and maybe even smile when they see it. A brand that does this well is Penn. (www.pennvita-example.com)
Nice to have
• I like 60's Mod Design if you need some inspiration. The packaging should also convey a sense of levity. Like you'll float or dance through life after drinking this.

```html
<!DOCTYPE html>
<html lang="en">
<head>
<meta charset="utf-8">
<title>Vemra – Mood-Boosting Energy Drink Mix</title>
<link rel="stylesheet" href="https://fonts.googleapis.com/css2?family=Montserrat:wght@400;500;700;800&display=swap">
<style>
  :root{
    --stage:#e9e9e9;
    --white:#ffffff;
    --silver:#e6e6ea;
    --crimson:#d42a5a;
    --gold:#e2a928;
    --gold-light:#f2c43c;
    --orange:#ee7325;
    --glass:#6fccea;
  }
  *{box-sizing:border-box;margin:0;padding:0}
  html,body{width:1200px;height:1200px;overflow:hidden;background:var(--stage)}
  body{font-family:"Montserrat",sans-serif;position:relative}

  .pouch{position:absolute;left:135px;top:275px;width:605px;height:685px;overflow:hidden;
    background:linear-gradient(180deg,var(--silver) 0%,var(--white) 18%,var(--white) 100%)}
  .pouch svg.pouch-bands{position:absolute;inset:0}
  .zip{position:absolute;left:25px;right:25px;height:3px;background:#d4d4d8;border-radius:2px}
  .zip-upper{top:88px}
  .zip-lower{top:100px}
  .brand{position:absolute;left:0;right:0;text-align:center;color:var(--orange);font-weight:700;line-height:1}
  .brand-name{top:98px;font-size:104px;letter-spacing:-2px}
  .brand-tag{top:193px;left:310px;right:auto;font-size:17px}
  .product{position:absolute;left:0;right:0;text-align:center;color:var(--crimson);line-height:1}
  .product-kicker{top:228px;font-size:25px;font-weight:500}
  .product-title{top:263px;font-size:40px;font-weight:800;line-height:1.02}
  .glass-art{position:absolute;left:265px;top:415px;width:150px;height:170px;border-radius:8px;
    background:linear-gradient(180deg,#e8848f 0%,var(--glass) 45%,#4fb8dd 100%)}
  .callouts-left{position:absolute;left:37px;top:400px;color:var(--gold-light);font-size:20px;line-height:23px}
  .callouts-left b{font-weight:700}
  .callouts-left .plus{padding-left:58px}
  .callouts-right{position:absolute;right:40px;top:475px;text-align:right;color:var(--gold-light);
    font-size:19px;font-weight:700;line-height:22px}
  .callouts-right .plus{padding-right:40px;font-weight:500}
  .flavor-tag{position:absolute;left:0;top:618px;height:40px;width:190px;background:var(--crimson);
    clip-path:polygon(0 0,94% 0,100% 50%,94% 100%,0 100%);color:#fff;font-weight:700;font-size:17px;
    line-height:40px;padding-left:25px;letter-spacing:.5px}
  .count{position:absolute;right:40px;top:618px;text-align:right;color:#fff}
  .count strong{display:block;font-size:19px;font-weight:700}
  .count span{font-size:14px}

  .stick{position:absolute;top:388px;width:150px;height:565px;overflow:hidden}
  .stick-1{left:752px}
  .stick-2{left:925px}
  .stick svg{position:absolute;inset:0}
  .stick-logo{position:absolute;left:122px;top:42px;transform-origin:0 0;transform:rotate(90deg);
    white-space:nowrap;color:var(--orange);line-height:1}
  .stick-logo .n{font-size:60px;font-weight:700;letter-spacing:-1px;display:block}
  .stick-logo .t{font-size:11px;font-weight:700;display:block;padding-left:62px;margin-top:2px}
  .stick-copy{position:absolute;left:124px;top:288px;transform-origin:0 0;transform:rotate(90deg);
    white-space:nowrap;color:#fff;line-height:1.2}
  .stick-copy .k{font-size:13px;font-weight:400;display:block}
  .stick-copy .h{font-size:15px;font-weight:800;display:block}
  .stick-copy .s{font-size:9.5px;font-weight:700;display:block;color:var(--gold-light)}
  .stick-copy .d{font-size:6.5px;display:block;color:var(--gold-light);line-height:1.3}
  .stick-flavor{position:absolute;left:0;right:0;top:500px;text-align:center;color:#fff;font-weight:800;
    font-size:16px;line-height:1.05}
</style>
</head>
<body>

<section class="pouch" aria-label="Vemra pouch front">
  <svg class="pouch-bands" viewBox="0 0 605 685" preserveAspectRatio="none">
    <polygon points="0,320 302,413 605,320 605,685 0,685" fill="var(--crimson)"/>
    <polygon points="0,265 302,358 605,265 605,290 302,383 0,290" fill="var(--gold)"/>
    <polygon points="0,290 302,383 605,290 605,302 302,395 0,302" fill="var(--white)"/>
    <polygon points="0,302 302,395 605,302 605,324 302,417 0,324" fill="var(--gold)"/>
    <rect x="0" y="600" width="605" height="85" fill="var(--gold)"/>
  </svg>
  <div class="zip zip-upper"></div>
  <div class="zip zip-lower"></div>

  <div class="brand brand-name">vemra</div>
  <div class="brand brand-tag">bright day spark</div>

  <div class="product product-kicker">MOOD-BOOSTING</div>
  <div class="product product-title">ENERGY DRINK<br>MIX</div>

  <div class="callouts-left">
    <b>Energy blend</b><br>80mg caffeine<br>taurine<br><span class="plus">+</span><br>
    <b>Happy blend</b><br>saffron<br>st. john's wort<br>rhodiola
  </div>

  <div class="glass-art" role="img" aria-label="Illustration of a drink stick pouring powder into a glass of water"></div>

  <div class="callouts-right">
    electrolytes<br><span class="plus">+</span><br>vitamins<br><span class="plus">+</span><br>0g sugar
  </div>

  <div class="flavor-tag">GOLDEN BERRY</div>
  <div class="count"><strong>16 sticks</strong><span>Net Wt. 4 oz. (114 g)</span></div>
</section>

<div class="stick stick-1" aria-label="Vemra drink stick">
  <svg viewBox="0 0 150 565" preserveAspectRatio="none">
    <rect x="0" y="0" width="150" height="565" fill="var(--white)"/>
    <polygon points="0,240 75,272 150,240 150,565 0,565" fill="var(--crimson)"/>
    <polygon points="0,230 75,262 150,230 150,240 75,272 0,240" fill="var(--gold)"/>
    <rect x="0" y="490" width="150" height="75" fill="var(--gold-light)"/>
  </svg>
  <div class="stick-logo"><span class="n">vemra</span><span class="t">bright day spark</span></div>
  <div class="stick-copy">
    <span class="k">MOOD-BOOSTING</span><span class="h">ENERGY DRINK MIX</span>
    <span class="s">electrolytes + vitamins + 0g sugar</span>
    <span class="d">Energy blend 80mg caffeine taurine</span>
    <span class="d">Happy blend saffron st. john's wort rhodiola</span>
  </div>
  <div class="stick-flavor">GOLDEN<br>BERRY</div>
</div>

<div class="stick stick-2" aria-label="Vemra drink stick">
  <svg viewBox="0 0 150 565" preserveAspectRatio="none">
    <rect x="0" y="0" width="150" height="565" fill="var(--white)"/>
    <polygon points="0,240 75,272 150,240 150,565 0,565" fill="var(--crimson)"/>
    <polygon points="0,230 75,262 150,230 150,240 75,272 0,240" fill="var(--gold)"/>
    <rect x="0" y="490" width="150" height="75" fill="var(--gold-light)"/>
  </svg>
  <div class="stick-logo"><span class="n">vemra</span><span class="t">bright day spark</span></div>
  <div class="stick-copy">
    <span class="k">MOOD-BOOSTING</span><span class="h">ENERGY DRINK MIX</span>
    <span class="s">electrolytes + vitamins + 0g sugar</span>
    <span class="d">Energy blend 80mg caffeine taurine</span>
    <span class="d">Happy blend saffron st. john's wort rhodiola</span>
  </div>
  <div class="stick-flavor">GOLDEN<br>BERRY</div>
</div>

</body>
</html>
```